business card for a shoe shop

we would like a business card for a family owned shoe shop.
With this information included.
Darnell's Shoe Store
Family owned since 1947

then on other side
Darnell's Shoe Store
Footwear fitting specialist
Phone: 9187 2630
218 Quarry St, Fernleigh Downs 3187
(cnr. Hartwick Rd and Quarry St)
darnellshoes218@examplemail.com
if could incorporate the purple color on card i have attached.

```html
<!DOCTYPE html>
<html lang="en">
<head>
<meta charset="utf-8">
<title>Darnell's Shoe Store – Business Card</title>
<link href="https://fonts.googleapis.com/css2?family=Lato:wght@400&display=swap" rel="stylesheet">
<style>
  :root {
    --brand-purple: #7563ab;
    --card-white: #ffffff;
    --backdrop-grey: #dfdfdf;
    --card-shadow: rgba(0, 0, 0, 0.45);
  }
  * { box-sizing: border-box; margin: 0; padding: 0; }
  html, body {
    width: 1200px;
    height: 1200px;
    overflow: hidden;
    background: var(--backdrop-grey);
    font-family: "Lato", sans-serif;
    color: var(--brand-purple);
  }
  .canvas {
    position: relative;
    width: 1200px;
    height: 1200px;
  }
  .card {
    position: absolute;
    background: var(--card-white);
    border: 7.5px solid var(--brand-purple);
    box-shadow: 0 4px 14px var(--card-shadow);
  }
  .card--front { left: 189px; top: 91px; width: 829px; height: 478px; }
  .card--back  { left: 187px; top: 639px; width: 834px; height: 478px; }

  .line {
    position: absolute;
    left: 0;
    right: 0;
    text-align: center;
    white-space: nowrap;
    line-height: 1;
  }
  .store-name {
    font-size: 69px;
    height: 69px;
    letter-spacing: -0.3px;
  }
  .tagline {
    display: flex;
    justify-content: center;
    align-items: center;
    font-size: 41px;
    height: 41px;
  }
  .tagline::before,
  .tagline::after {
    content: "";
    display: block;
    width: 35px;
    height: 3.5px;
    background: var(--brand-purple);
  }
  .tagline::before { margin-right: 2px; }
  .tagline::after  { margin-left: 2px; }

  .contact {
    font-size: 33px;
    height: 33px;
  }

  .card--front .store-name { top: 58px; }
  .card--front .tagline    { top: 142px; }
  .contact--phone   { top: 262px; }
  .contact--address { top: 307px; }
  .contact--corner  { top: 351px; }
  .contact--email   { top: 396px; }

  .card--back .store-name { top: 173px; }
  .card--back .tagline    { top: 256px; }
</style>
</head>
<body>
<main class="canvas">
  <section class="card card--front" aria-label="Card front">
    <h1 class="line store-name">Darnell's Shoe Store</h1>
    <p class="line tagline">Footwear fitting specialist</p>
    <p class="line contact contact--phone">Phone: 9187 2630</p>
    <p class="line contact contact--address">218 Quarry St, Fernleigh Downs 3187</p>
    <p class="line contact contact--corner">(cnr. Hartwick Rd and Quarry St)</p>
    <p class="line contact contact--email">darnellshoes218@examplemail.com</p>
  </section>

  <section class="card card--back" aria-label="Card back">
    <h2 class="line store-name">Darnell's Shoe Store</h2>
    <p class="line tagline">Family owned since 1947</p>
  </section>
</main>
</body>
</html>
```